Business cards for modern animal non-profit organization
Vastrel Foundation
Business cards for modern animal non-profit organization - Animals
Creative Brief
Professional
Mirabel T. Ashgrove
President, Founder
no address
mirabel@vastrel.org
www.vastrel.org
501(c)3 non-profit # 84-6159203
Name of organization: Vastrel Foundation Would like to add the phrase: 'Improving the lives of Asian elephants and the people connected to them.' Perhaps a split look, the quote on the left, info on the right.
I have a photo I would like to use on the back side with the logo.
mirabel mirabel
Site Admin, Fairly sure I uploaded the .ai file of my logo. Please let me know if I need to do anything else.
tidewarp tidewarp
Forgot to mention. Please no cartoon elephants. Not needed. Please check out my website to see the our style. www.vastrel.org I do not like the font you see for 'vastrel' in blue on the website. Please do not use that. I prefer the elegant look of the font on my logo. Thanks

```html
<!DOCTYPE html>
<html lang="en">
<head>
<meta charset="utf-8">
<title>Vastrel Foundation — Business Cards</title>
<link rel="stylesheet" href="https://fonts.googleapis.com/css2?family=EB+Garamond:ital,wght@0,400;0,600;1,400&display=swap">
<style>
  :root {
    --backdrop: #e6e4e0;
    --card-white: #ffffff;
    --ink: #2b2b2b;
    --ink-soft: #555555;
    --brand-blue: #3d7fb8;
    --mark-dark: #23282c;
    --rule: #b9b9b9;
    --photo-light: #d9d5cf;
    --photo-mid: #a89f94;
    --photo-dark: #6f665c;
  }
  * { box-sizing: border-box; margin: 0; padding: 0; }
  html, body {
    width: 1200px; height: 869px; overflow: hidden;
    background: var(--backdrop);
    font-family: "EB Garamond", Georgia, serif;
    color: var(--ink);
  }
  .sheet {
    width: 1200px; height: 869px;
    display: flex; align-items: center; justify-content: center; gap: 40px;
  }
  .card {
    position: relative;
    width: 540px; height: 309px;
    border-radius: 12px;
    overflow: hidden;
    background: var(--card-white);
    box-shadow: 0 4px 14px rgba(0,0,0,0.15);
  }

  /* Front */
  .front-photo {
    position: absolute; left: 0; top: 0; width: 62%; height: 100%;
    background: linear-gradient(100deg, var(--photo-mid) 0%, var(--photo-light) 55%, rgba(255,255,255,0) 100%);
    opacity: 0.35;
  }
  .brand {
    position: absolute; top: 22px; right: 42px;
    display: flex; flex-direction: column; align-items: center; gap: 8px;
  }
  .brand-dot {
    width: 56px; height: 56px; border-radius: 50%;
    background: var(--mark-dark);
  }
  .brand-name {
    font-weight: 400; color: var(--brand-blue);
    text-transform: uppercase; letter-spacing: 0.2em;
    font-size: 18px; line-height: 1.15; text-align: center;
  }
  .contact {
    position: absolute; left: 30px; top: 160px;
  }
  .contact .name {
    color: var(--brand-blue); font-weight: 600; font-size: 17px; line-height: 1.2;
  }
  .contact .role { font-size: 11px; color: var(--ink-soft); line-height: 1.3; }
  .quote {
    position: absolute; right: 30px; top: 148px;
    font-size: 13.5px; line-height: 1.3; text-align: right; color: var(--ink);
    white-space: nowrap;
  }
  .quote .highlight { color: var(--brand-blue); }
  .divider {
    position: absolute; left: 26px; right: 26px; top: 212px;
    border-top: 1px solid var(--rule);
  }
  .contact-lines {
    position: absolute; left: 30px; top: 222px;
    font-size: 10px; line-height: 1.45; color: var(--ink-soft);
  }
  .license {
    position: absolute; left: 30px; bottom: 22px;
    font-size: 10px; color: var(--ink-soft);
  }

  /* Back */
  .back-photo {
    position: absolute; inset: 0;
    background: radial-gradient(ellipse at 30% 40%, var(--photo-mid) 0%, var(--photo-dark) 55%, #514a43 100%);
  }
  .back-fade {
    position: absolute; inset: 0;
    background: linear-gradient(135deg, rgba(255,255,255,0) 40%, rgba(240,238,234,0.75) 85%);
  }
  .back-brand {
    position: absolute; right: 50px; bottom: 34px;
    display: flex; flex-direction: column; align-items: center; gap: 8px;
  }
  .back-brand .brand-dot { background: var(--card-white); width: 64px; height: 64px; }
</style>
</head>
<body>
<main class="sheet">
  <section class="card card-front">
    <div class="front-photo" role="img" aria-label="Faint close-up photograph of an Asian elephant's eye and wrinkled skin"></div>
    <div class="brand">
      <span class="brand-dot"></span>
      <p class="brand-name">Vastrel<br>Foundation</p>
    </div>
    <div class="contact">
      <p class="name">Mirabel T. Ashgrove</p>
      <p class="role">President, Founder</p>
    </div>
    <p class="quote">“Improving the lives of <span class="highlight">Asian</span><br><span class="highlight">Elephants</span> and the people<br>connected to them.”</p>
    <div class="divider"></div>
    <div class="contact-lines">
      <p>mirabel@vastrel.org</p>
      <p>www.vastrel.org</p>
    </div>
    <p class="license">License No. 501(c)3 non-profit # 84-6159203</p>
  </section>

  <section class="card card-back">
    <div class="back-photo" role="img" aria-label="Full-bleed close-up photograph of an Asian elephant's eye and textured skin"></div>
    <div class="back-fade"></div>
    <div class="back-brand">
      <span class="brand-dot"></span>
      <p class="brand-name">Vastrel<br>Foundation</p>
    </div>
  </section>
</main>
</body>
</html>
```